Z-Reel Carnival Podcast Cover Design

We need a podcast cover (square design) for a podcast called Z-Reel Carnival.
MANDATORY: Z-REEL CARNIVAL
OPTIONAL: with The Creature Nerd Dale Furnow

Z-Reel Carnival is a movie podcast dedicated to covering all of the cult oddities you saw in theaters and video stores as a kid but never got to rent or watch. Focusing on obscure horror, cult oddities, action movies, exploitation movies, foreign knockoffs, and more, this a show designed to help you take a trip down memory lane or find new weird movies to add to your streaming queue. Come take a walk on the wild side of cinema at Z-Reel Carnival,..where one person's trash movie is our treasure.
##
Fonts that fit the vibe we're going for:
https://www.typevault.example/sets/grindhouse-drip-font-kelvorn-studio
https://www.pinboardly.example/pin/481926035517204963/
https://www.typevault.example/sets/grindhouse-vintage-font-kelvorn-studio

Target Market(s)

Primarily male, although we have some female fans as well. Podcast fans of B-movies (inexpensively made and a bit outrageous), cult movies, weird movies, old movies, horror movies, and action films.

Industry/Entity Type

Media - Movies -Podcast

Font styles to use
Other font styles liked:
• Fonts that fit the vibe: Fonts: https://www.typevault.example/sets/grindhouse-drip-font-kelvorn-studio https://www.pinboardly.example/pin/481926035517204963/ https://www.typevault.example/sets/grindhouse-vintage-font-kelvorn-studio

Colors
EB3D1F
EC4F4E
F09395
F8D3D4
FCEDEE

Requirements
Must have
• Z-REEL CARNIVAL
Nice to have
• 1) with The Creature Nerd Dale Furnow; 2) VISUALS: VHS tapes

```html
<!DOCTYPE html>
<html lang="en">
<head>
<meta charset="utf-8">
<title>Z-Reel Carnival — Podcast Cover</title>
<link rel="stylesheet" href="https://fonts.googleapis.com/css2?family=Bangers&family=Special+Elite&display=swap">
<style>
  :root {
    --ink-black: #050505;
    --splatter-red: #eb3d1f;
    --blood-red: #e8141a;
    --ash-grey: #8a8a8a;
    --bone-white: #f4f4f4;
  }
  html, body {
    margin: 0;
    padding: 0;
    width: 1200px;
    height: 1200px;
    overflow: hidden;
    background: var(--ink-black);
  }
  .cover {
    position: relative;
    width: 1200px;
    height: 1200px;
    overflow: hidden;
    background: var(--ink-black);
  }
  .cover__texture {
    position: absolute;
    inset: 0;
    background:
      radial-gradient(ellipse 420px 300px at 120px 140px, rgba(232, 20, 26, 0.85), transparent 70%),
      radial-gradient(ellipse 500px 200px at 520px 60px, rgba(232, 20, 26, 0.55), transparent 75%),
      radial-gradient(ellipse 380px 180px at 900px 90px, rgba(138, 138, 138, 0.35), transparent 75%),
      radial-gradient(ellipse 260px 520px at 1050px 800px, rgba(232, 20, 26, 0.28), transparent 75%),
      radial-gradient(ellipse 300px 500px at 250px 900px, rgba(232, 20, 26, 0.22), transparent 75%),
      linear-gradient(180deg, #1a0505 0%, var(--ink-black) 45%, #120303 100%);
  }
  .cover__title {
    position: absolute;
    inset: 0;
    width: 1200px;
    height: 1200px;
  }
  .cover__title text {
    font-family: "Bangers", "Impact", sans-serif;
    fill: var(--bone-white);
  }
  .cover__credits {
    position: absolute;
    left: 0;
    right: 0;
    top: 900px;
    font-family: "Special Elite", "Courier New", monospace;
    text-align: center;
    line-height: 1;
  }
  .credits__with {
    position: absolute;
    left: 560px;
    top: 0;
    font-size: 70px;
    color: var(--blood-red);
  }
  .credits__host-title,
  .credits__host-name {
    position: absolute;
    color: var(--bone-white);
    font-size: 74px;
    white-space: nowrap;
  }
  .credits__host-title { left: 272px; top: 88px; }
  .credits__host-name { left: 334px; top: 180px; }
</style>
</head>
<body>
  <main class="cover">
    <div class="cover__texture" role="img" aria-label="Dark background with red and grey blood-splatter drips and streaked smear texture"></div>

    <svg class="cover__title" viewBox="0 0 1200 1200" aria-label="Z-REEL CARNIVAL">
      <g transform="rotate(-10.5 100 621)">
        <text class="title__line" x="100" y="621" font-size="360" textLength="1000" lengthAdjust="spacingAndGlyphs">Z-REEL</text>
      </g>
      <g transform="rotate(-10.5 100 895)">
        <text class="title__line" x="100" y="895" font-size="360" textLength="1010" lengthAdjust="spacingAndGlyphs">CARNIVAL</text>
      </g>
    </svg>

    <div class="cover__credits">
      <span class="credits__with">with</span>
      <span class="credits__host-title">The Creature Nerd</span>
      <span class="credits__host-name">Dale Furnow</span>
    </div>
  </main>
</body>
</html>
```